Expense Tracker App for Young Adults

I need a mobile app designer to design an app UI for me. It is for an expense tracker app. I’ve attached a mind map of the various screens and features of the app.

I would like to see designs for this app which is targeted towards young adults (late teens & early 20s) just starting their career who want to plan their budgets and track their expenses.
Updates

Hello designers! I'm conscious that this is not a guaranteed project, so I can understand that some of you might be apprehensive. Just wanted to let you know that I'm willing to see your initial drafts that show your direction and theme for design. You don't have to design the whole app. In fact, it's better if you share your initial design ideas so that we can have a discussion and I can give my input. If I see some good initial designs, I will be happy to make this a guaranteed project. I'm simply being cautious since I'm bootstrapping this and funding out of my own pocket. Thank you for your understanding!

Target Market(s)

Young adults who are just starting their careers, late teens and early 20s.

Font styles to use
Sans Serif

Requirements
Must have
• Ease of use, smart and sleek, a guided setup wizard which will help users setup their account after signing up.
Should not have
• Clunky

```html
<!DOCTYPE html>
<html lang="en">
<head>
<meta charset="utf-8">
<title>Expense Tracker – Login and Categories</title>
<link href="https://fonts.googleapis.com/css2?family=Nunito+Sans:wght@400;600;700;800&display=swap" rel="stylesheet">
<style>
  :root {
    --page-bg: #ECECF7;
    --screen-bg: #1E1E28;
    --card-bg: #1A1A22;
    --field-line: #3A3A46;
    --text-main: #FFFFFF;
    --text-soft: #D6D6DE;
    --text-muted: #8A8A98;
    --accent: #5500FF;
    --accent-glow: rgba(85, 0, 255, 0.45);
    --drinks: #E8241E;
    --travel: #12C8E8;
    --cloths: #3DA84A;
    --jewelry: #1E4BEB;
    --electronics: #F2E41A;
    --health: #6A12F0;
  }
  * { box-sizing: border-box; margin: 0; padding: 0; }
  html, body {
    width: 1200px; height: 1083px; overflow: hidden;
    background: var(--page-bg);
    font-family: "Nunito Sans", Arial, sans-serif;
    color: var(--text-main);
  }
  .canvas { position: relative; width: 1200px; height: 1083px; }

  .screen {
    position: absolute; top: 143px;
    width: 367px; height: 794px;
    background: var(--screen-bg);
    border-radius: 44px;
    overflow: hidden;
  }
  .screen--login { left: 167px; }
  .screen--categories { left: 668px; }

  .screen-title {
    position: absolute; left: 35px; top: 88px;
    font-size: 32px; font-weight: 700; letter-spacing: 0.3px;
  }

  /* Login */
  .welcome { position: absolute; left: 35px; top: 140px; font-size: 11px; color: var(--text-soft); }
  .intro { position: absolute; left: 35px; top: 160px; font-size: 13px; color: var(--text-soft); }

  .field {
    position: absolute; left: 35px; width: 296px; height: 50px;
    border: 1px solid var(--field-line); border-radius: 4px;
  }
  .field--username { top: 247px; }
  .field--password { top: 339px; }
  .field-label {
    position: absolute; left: 30px; top: -8px;
    padding: 0 13px; background: var(--screen-bg);
    font-size: 11px; color: var(--text-soft); line-height: 14px;
  }
  .field-icon { position: absolute; right: 14px; top: 17px; }

  .faceid-button {
    position: absolute; left: 37px; top: 412px; width: 60px; height: 40px;
    background: #1B1B23; border-radius: 6px;
    box-shadow: 0 6px 14px rgba(0,0,0,0.35);
    display: flex; align-items: center; justify-content: center;
  }
  .primary-button {
    position: absolute; left: 167px; top: 412px; width: 165px; height: 40px;
    background: var(--accent); border-radius: 6px;
    box-shadow: 0 8px 18px var(--accent-glow);
    font-size: 11px; font-weight: 700;
    display: flex; align-items: center; justify-content: center;
  }
  .primary-button svg { position: absolute; right: 14px; top: 13px; }

  .forgot-link {
    position: absolute; right: 39px; top: 497px;
    font-size: 11px; font-weight: 700; letter-spacing: 0.3px;
  }
  .social-divider {
    position: absolute; left: 35px; top: 573px; width: 296px;
    display: flex; align-items: center; gap: 16px;
    font-size: 11px; color: var(--text-muted);
  }
  .social-divider::after { content: ""; flex: 1; height: 1px; background: var(--field-line); }

  .social-button {
    position: absolute; top: 629px; width: 136px; height: 40px;
    background: var(--accent); border-radius: 6px;
    box-shadow: 0 8px 18px var(--accent-glow);
    display: flex; align-items: center; padding: 0 16px; gap: 10px;
    font-size: 11px; font-weight: 700;
  }
  .social-button--linkup { left: 35px; }
  .social-button--chirply { left: 195px; }
  .social-mark { width: 12px; height: 12px; border-radius: 50%; background: var(--text-main); flex: none; }
  .social-name { flex: 1; text-align: right; }

  .signup-line {
    position: absolute; left: 0; right: 0; top: 752px; text-align: center;
    font-size: 11px; color: var(--text-soft);
  }
  .signup-line strong { font-size: 13px; font-weight: 700; color: var(--text-main); margin-left: 4px; }

  /* Categories */
  .category-card {
    position: absolute; width: 123px; height: 158px;
    background: var(--card-bg); border-radius: 12px;
    box-shadow: 0 8px 18px rgba(0,0,0,0.25);
  }
  .col-1 { left: 35px; } .col-2 { left: 196px; }
  .row-1 { top: 180px; } .row-2 { top: 373px; } .row-3 { top: 565px; }
  .category-art {
    position: absolute; left: 34px; top: 10px; width: 88px; height: 86px;
    border-radius: 10px; opacity: 0.9;
  }
  .art--drinks { background: linear-gradient(135deg, var(--drinks), #8E1512); }
  .art--travel { background: linear-gradient(135deg, var(--travel), #0A7A90); }
  .art--cloths { background: linear-gradient(135deg, var(--cloths), #1F5E28); }
  .art--jewelry { background: linear-gradient(135deg, var(--jewelry), #122C8C); }
  .art--electronics { background: linear-gradient(135deg, var(--electronics), #8E850E); }
  .art--health { background: linear-gradient(135deg, var(--health), #3A0A88); }
  .category-name {
    position: absolute; left: 0; right: 0; top: 124px; text-align: center;
    font-size: 11px; font-weight: 700;
  }
  .category-name--light { font-weight: 400; }

  .menu-bar {
    position: absolute; left: 0; bottom: 0; width: 100%; height: 64px;
    background: var(--accent);
    display: flex; align-items: center; justify-content: flex-end;
    padding: 0 26px 16px 0; gap: 18px;
    font-size: 11px; font-weight: 700;
  }
</style>
</head>
<body>
<div class="canvas">

  <section class="screen screen--login" aria-label="Login screen">
    <h1 class="screen-title">Login</h1>
    <p class="welcome">Welcome back!</p>
    <p class="intro">Please login to access expences</p>

    <div class="field field--username"><span class="field-label">Username</span></div>
    <div class="field field--password">
      <span class="field-label">Password</span>
      <svg class="field-icon" width="22" height="14" viewBox="0 0 22 14" fill="none" stroke="#8A8A98" stroke-width="1.4">
        <path d="M1 7C4 2 8 1 11 1s7 1 10 6c-3 5-7 6-10 6S4 12 1 7z"/>
        <circle cx="11" cy="7" r="2.6"/>
      </svg>
    </div>

    <div class="faceid-button" aria-label="Face login">
      <svg width="30" height="30" viewBox="0 0 30 30" fill="none" stroke="#E6E6EE" stroke-width="1.8" stroke-linecap="round">
        <path d="M2 9V5a3 3 0 0 1 3-3h4M21 2h4a3 3 0 0 1 3 3v4M28 21v4a3 3 0 0 1-3 3h-4M9 28H5a3 3 0 0 1-3-3v-4"/>
        <path d="M10 10v2M20 10v2M15 10v6h-1.5M10 20c3 2.5 7 2.5 10 0"/>
      </svg>
    </div>
    <div class="primary-button">Login
      <svg width="16" height="14" viewBox="0 0 16 14" fill="none" stroke="#FFFFFF" stroke-width="1.4" stroke-linecap="round">
        <path d="M1 7h14M9 1l6 6-6 6"/>
      </svg>
    </div>

    <p class="forgot-link">Forgot Password ?</p>
    <div class="social-divider">Or login with social accounts</div>

    <div class="social-button social-button--linkup"><span class="social-mark"></span><span class="social-name">Linkup</span></div>
    <div class="social-button social-button--chirply"><span class="social-mark"></span><span class="social-name">Chirply</span></div>

    <p class="signup-line">Don’t have an account with us? <strong>Sign Up</strong></p>
  </section>

  <section class="screen screen--categories" aria-label="Categories screen">
    <h1 class="screen-title">Categories</h1>

    <div class="category-card col-1 row-1">
      <div class="category-art art--drinks" role="img" aria-label="Neon line icon of a cocktail glass"></div>
      <p class="category-name">Drinks</p>
    </div>
    <div class="category-card col-2 row-1">
      <div class="category-art art--travel" role="img" aria-label="Neon line icon of travel suitcases"></div>
      <p class="category-name">Travel</p>
    </div>
    <div class="category-card col-1 row-2">
      <div class="category-art art--cloths" role="img" aria-label="Neon line icon of a jacket"></div>
      <p class="category-name">Cloths</p>
    </div>
    <div class="category-card col-2 row-2">
      <div class="category-art art--jewelry" role="img" aria-label="Neon line icon of a sparkling diamond"></div>
      <p class="category-name">Jewelry</p>
    </div>
    <div class="category-card col-1 row-3">
      <div class="category-art art--electronics" role="img" aria-label="Neon line icon of a screen and game controller"></div>
      <p class="category-name category-name--light">Electronics</p>
    </div>
    <div class="category-card col-2 row-3">
      <div class="category-art art--health" role="img" aria-label="Neon line icon of a dumbbell"></div>
      <p class="category-name">Health</p>
    </div>

    <nav class="menu-bar">
      <svg width="28" height="10" viewBox="0 0 28 10" fill="none" stroke="#FFFFFF" stroke-width="2" stroke-linecap="round">
        <path d="M1 1h26M6 9h21"/>
      </svg>
      <span>menu</span>
    </nav>
  </section>

</div>
</body>
</html>
```